E-commerce website needs a splash page ad

Our website, tinkerloft.com, needs an additional ad on our 'splash page'. It needs to fit within these dimensions: 980x383 pixels.

Please visit tinkerloft.com to see the slide in action, and to see what content already exists.

The splash ad needs to contain an image of the Dr. Glowfin product we are selling, as well as the Dr Glowfin logo featured in one of the corners of the ad. A button need to be made (visual only) with the text "view page" or something akin to "take me to part of the website that sells this product"

The ad needs to be clean, modern, and aimed towards a mature audience- no flowery graphics are needed.

Target Market(s)

Families, senior citizens, homeowners, small business owners

Industry/Entity Type

Product

Font styles to use
Sans Serif

Colors

Designer to choose colors to be used in the design.

Requirements
Must have
• -Black background with large, white font that says (in one way or another) " outdoor motion detection lighting"
-Dr Glowfin logo must be present in one of the 4 corners
-must fit the 980x383 pixels size
-A light gray-to-white gradient somewhere in the background
- At least 2 Dr. Glowfin images must be used (a white and black dr glowfin, for example)
Nice to have
• -A cone-shaped white gradient emitting from one of the Dr. Glowfin spotlights
- This white gradient will 'illuminate' a "view page" button (or 'buy now', etc)

```html
<!DOCTYPE html>
<html lang="en">
<head>
<meta charset="utf-8">
<title>Outdoor Motion Detection Lighting</title>
<link href="https://fonts.googleapis.com/css2?family=Montserrat:wght@600;700;800&display=swap" rel="stylesheet">
<style>
  :root {
    --ink: #000000;
    --white: #ffffff;
    --green: #8cc63f;
    --green-glow: #3dff6a;
    --button-top: #6cc04a;
    --button-bottom: #2f8a1c;
    --violet: #8a3dff;
    --product-light: #e9ecee;
    --product-dark: #2a2d30;
  }
  * { margin: 0; padding: 0; box-sizing: border-box; }
  html, body { width: 1200px; height: 469px; overflow: hidden; background: var(--ink); }
  .ad {
    position: relative;
    width: 1200px;
    height: 469px;
    overflow: hidden;
    font-family: "Montserrat", sans-serif;
    background:
      radial-gradient(ellipse 260px 60px at 470px 110px, rgba(61,255,106,0.55), transparent 70%),
      radial-gradient(ellipse 420px 30px at 420px 175px, rgba(61,255,106,0.35), transparent 75%),
      radial-gradient(ellipse 500px 14px at 300px 140px, rgba(138,61,255,0.35), transparent 80%),
      radial-gradient(ellipse 300px 180px at 860px 60px, rgba(61,255,106,0.25), transparent 70%),
      var(--ink);
  }
  .beam { position: absolute; inset: 0; }
  .headline {
    position: absolute;
    left: 27px;
    top: 44px;
    color: var(--white);
    font-weight: 700;
    font-size: 57px;
    line-height: 67px;
    letter-spacing: 0.5px;
    text-transform: uppercase;
  }
  .headline .accent { color: var(--green); }
  .cta {
    position: absolute;
    left: 135px;
    top: 272px;
    width: 251px;
    height: 66px;
    border-radius: 4px;
    background: linear-gradient(var(--button-top), var(--button-bottom));
    color: var(--white);
    font-weight: 700;
    font-size: 27px;
    display: flex;
    align-items: center;
    justify-content: center;
    box-shadow: 0 2px 6px rgba(0,0,0,0.35);
  }
  .tagline {
    position: absolute;
    left: 34px;
    top: 433px;
    color: var(--white);
    font-weight: 700;
    font-size: 23px;
    text-transform: uppercase;
  }
  .brand {
    position: absolute;
    left: 700px;
    top: 420px;
    color: var(--green);
    font-weight: 800;
    font-size: 38px;
    letter-spacing: 1px;
  }
  .product { position: absolute; }
  .product-white {
    left: 805px; top: 22px; width: 165px; height: 178px;
    border-radius: 48% 48% 40% 40%;
    background: radial-gradient(circle at 40% 35%, var(--white), var(--product-light) 55%, #b9bec2);
  }
  .product-black {
    left: 905px; top: 135px; width: 330px; height: 360px;
    border-radius: 45% 30% 30% 45%;
    background: radial-gradient(circle at 35% 40%, #f4f6f7 0 18%, #5d6266 30%, var(--product-dark) 60%, #0c0d0e);
  }
</style>
</head>
<body>
  <div class="ad">
    <svg class="beam" width="1200" height="469" viewBox="0 0 1200 469" aria-hidden="true">
      <defs>
        <linearGradient id="beamFill" x1="0" y1="0" x2="1" y2="0">
          <stop offset="0" stop-color="#ffffff" stop-opacity="0.88"/>
          <stop offset="0.7" stop-color="#ffffff" stop-opacity="0.96"/>
          <stop offset="1" stop-color="#ffffff" stop-opacity="1"/>
        </linearGradient>
        <linearGradient id="beamEdge" x1="0" y1="0" x2="0" y2="1">
          <stop offset="0" stop-color="#d9d9d9" stop-opacity="0.9"/>
          <stop offset="0.5" stop-color="#ffffff" stop-opacity="1"/>
          <stop offset="1" stop-color="#cfcfcf" stop-opacity="0.9"/>
        </linearGradient>
      </defs>
      <polygon points="0,208 980,248 980,318 0,368" fill="url(#beamEdge)" opacity="0.9"/>
      <polygon points="0,215 980,252 980,312 0,360" fill="url(#beamFill)"/>
    </svg>

    <h1 class="headline">Outdoor <span class="accent">Motion</span><br>Detection Lighting</h1>

    <div class="cta">LEARN MORE</div>

    <p class="tagline">Surprisingly bright light anywhere</p>

    <div class="product product-white" role="img" aria-label="White Dr Glowfin motion sensor spotlight mounted on a bracket"></div>
    <div class="product product-black" role="img" aria-label="Black Dr Glowfin motion sensor spotlight shining its beam to the left"></div>

    <div class="brand">Dr Glowfin</div>
  </div>
</body>
</html>
```